Copper Lantern LLC Business Card

We need a business card design for a newco in Texas. We are a team of professionals who join start ups as founders and help launch their businesses, which are primarily related to food and beverage and the service side of the industry. We love local and craft and are partners in businesses in the local meat, BBQ and Burger, fine dining, and beverage alcohol businesses. Our specialty is finance and the business side of start ups, including assisting with capital raises as principals, not brokers. We do not currently have any logos or graphics for this entity. Our values include helping people succeed, rooting for the underdog, healthy food, the environment and being good citizens.

Target Market(s)

Everybody but also Angel Investors, CPAs, Bankers, Entrepreneurs

Industry/Entity Type

Business

Contact Information for Business Card

Fields for Business Name, Title, Email Address, Phone Number. Place to add mailing address and web domain later.

Font styles to use
Sans Serif

Colors

Designer to choose colors to be used in the design.

Requirements
Should not have
• Pictures of booze bottles or drinks thought there could be a social scene that does not strictly focus on those. No cows, cowboy hats or ranches. We are not a Wall Street type entity so no huge office buildings or skylines.

```html
<!DOCTYPE html>
<html lang="en">
<head>
<meta charset="utf-8">
<title>Copper Lantern LLC Business Card</title>
<link href="https://fonts.googleapis.com/css2?family=Oswald:wght@700&family=Open+Sans:wght@400;600&display=swap" rel="stylesheet">
<style>
  :root {
    --page-bg: #e9e4dc;
    --card-deep: #c2530f;
    --card-mid: #e98a1c;
    --card-light: #f3c232;
    --accent-yellow: #ffd21f;
    --ink: #1a1208;
    --band: #0d0a06;
    --photo-warm-a: #8a3b12;
    --photo-warm-b: #e0a13c;
    --photo-cool-a: #6c4a2a;
    --photo-cool-b: #c9a065;
  }
  * { margin: 0; padding: 0; box-sizing: border-box; }
  html, body { width: 1200px; height: 780px; overflow: hidden; background: var(--page-bg); }
  .canvas { position: relative; width: 1200px; height: 780px; }
  .card {
    position: absolute; left: 100px; top: 105px; width: 1000px; height: 570px;
    border-radius: 6px; overflow: hidden;
    box-shadow: 0 14px 30px rgba(0,0,0,.25);
  }
  .card-art { position: absolute; inset: 0; width: 100%; height: 100%; }
  .company-name {
    position: absolute; left: 40px; top: 232px; width: 420px;
    font-family: "Oswald", sans-serif; font-weight: 700; font-size: 50px; line-height: 1.1;
    color: var(--accent-yellow); white-space: nowrap;
    -webkit-text-stroke: 1.5px var(--ink);
  }
  .person { position: absolute; left: 480px; top: 262px; width: 180px; }
  .person-name {
    font-family: "Oswald", sans-serif; font-weight: 700; font-size: 34px; white-space: nowrap;
    color: var(--accent-yellow); line-height: 1.05; -webkit-text-stroke: 1px var(--ink);
  }
  .person-title {
    font-family: "Open Sans", sans-serif; font-size: 24px; color: var(--ink); margin-top: 2px;
  }
  .contact {
    position: absolute; left: 690px; top: 272px;
    font-family: "Open Sans", sans-serif; font-size: 20px; color: var(--ink); line-height: 1.35;
    white-space: nowrap;
  }
  .contact-row { display: flex; align-items: center; gap: 8px; }
  .contact-icon { width: 18px; height: 18px; flex: none; }
</style>
</head>
<body>
<div class="canvas">
  <div class="card">
    <svg class="card-art" viewBox="0 0 1000 570" xmlns="http://www.w3.org/2000/svg">
      <defs>
        <linearGradient id="cardGlow" x1="0" y1="0" x2="1" y2="0.4">
          <stop offset="0" stop-color="var(--card-deep)"/>
          <stop offset="0.5" stop-color="var(--card-mid)"/>
          <stop offset="1" stop-color="var(--card-light)"/>
        </linearGradient>
        <linearGradient id="skewerTones" x1="0" y1="0" x2="1" y2="1">
          <stop offset="0" stop-color="var(--photo-warm-b)"/>
          <stop offset="1" stop-color="var(--photo-warm-a)"/>
        </linearGradient>
        <linearGradient id="burgerTones" x1="0" y1="0" x2="1" y2="1">
          <stop offset="0" stop-color="var(--photo-cool-b)"/>
          <stop offset="1" stop-color="var(--photo-cool-a)"/>
        </linearGradient>
      </defs>
      <rect class="card-base" width="1000" height="570" fill="url(#cardGlow)"/>

      <path class="band-top" d="M400 0 C470 170 760 260 1000 240 L1000 268 C740 290 440 200 372 0 Z" fill="var(--band)"/>
      <path class="photo-skewer" role="img" aria-label="Grilled meat and pepper skewer over a fire"
            d="M420 0 C490 160 770 245 1000 225 L1000 0 Z" fill="url(#skewerTones)"/>

      <path class="band-bottom" d="M0 390 C140 380 480 400 640 570 L610 570 C460 420 140 405 0 415 Z" fill="var(--band)"/>
      <path class="photo-burger" role="img" aria-label="Burger with bacon, onion rings and fries"
            d="M0 412 C140 402 455 420 600 570 L0 570 Z" fill="url(#burgerTones)"/>
    </svg>

    <div class="company-name">Copper Lantern LLC</div>

    <div class="person">
      <div class="person-name">Dana Reyes</div>
      <div class="person-title">Owner</div>
    </div>

    <div class="contact">
      <div class="contact-row">PO BOX 418 Alder Road</div>
      <div class="contact-row">Austin, Texas USA</div>
      <div class="contact-row">
        <svg class="contact-icon" viewBox="0 0 20 20"><rect width="20" height="20" rx="2" fill="var(--ink)"/><path d="M6 4 L8 4 L9 7 L7.5 8.5 C8.5 10.5 9.5 11.5 11.5 12.5 L13 11 L16 12 L16 14 C16 15 15 16 14 16 C9 15.5 4.5 11 4 6 C4 5 5 4 6 4 Z" fill="var(--accent-yellow)"/></svg>
        512 555 0147
      </div>
      <div class="contact-row">
        <svg class="contact-icon" viewBox="0 0 20 20"><rect width="20" height="20" rx="2" fill="var(--ink)"/><rect x="3.5" y="5.5" width="13" height="9" fill="none" stroke="var(--accent-yellow)" stroke-width="1.4"/><path d="M3.5 5.5 L10 11 L16.5 5.5" fill="none" stroke="var(--accent-yellow)" stroke-width="1.4"/></svg>
        hello@copperlantern.co
      </div>
      <div class="contact-row">
        <svg class="contact-icon" viewBox="0 0 20 20"><circle cx="10" cy="10" r="9.5" fill="var(--ink)"/><circle cx="10" cy="10" r="6.5" fill="none" stroke="var(--accent-yellow)" stroke-width="1.2"/><ellipse cx="10" cy="10" rx="3" ry="6.5" fill="none" stroke="var(--accent-yellow)" stroke-width="1.2"/><path d="M3.5 10 H16.5" stroke="var(--accent-yellow)" stroke-width="1.2"/></svg>
        www.copperlantern.co
      </div>
    </div>
  </div>
</div>
</body>
</html>
```